CD Cover Art for Breakout Album

I'm looking for cover art for my album that is in the "Americana" genre. It has some songs that are a little towards hard rock, but a couple are softer ballads as well. The album is called "Lanterns, Orchards, and Harvests," focusing on the after-effects of combat on the ones that serve. I want to integrate red, white and blue themes that are not pandering or kitchy. If possible, I would like to subtly integrate the "battlefield cross" which is attached as an image. I would like it to be as simple as possible, and don't want it solely military focused because the album is a collection of stories, only a few of which are explicitly military.

```html
<!DOCTYPE html>
<html lang="en">
<head>
<meta charset="utf-8">
<title>Lanterns, Orchards, and Harvests — Daniel Harrow</title>
<link rel="stylesheet" href="https://fonts.googleapis.com/css2?family=Montserrat:wght@300;700&display=swap">
<style>
  :root {
    --night: #07060f;
    --sky-deep: #0b2487;
    --sky-mid: #2f47a6;
    --dusk-violet: #8a78b4;
    --dusk-rose: #c99aa8;
    --sunset-peach: #e2a683;
    --sunset-orange: #cf6f3a;
    --ember: #7a2a2a;
    --frame: #ffffff;
    --title: #ffffff;
    --artist: #e8284a;
  }
  html, body {
    margin: 0;
    padding: 0;
    width: 1200px;
    height: 1200px;
    overflow: hidden;
    background: #ffffff;
  }
  .album-cover {
    position: relative;
    width: 1200px;
    height: 1200px;
    background: var(--night);
    overflow: hidden;
  }
  .cover-photo {
    position: absolute;
    left: 0;
    top: 0;
    width: 1200px;
    height: 920px;
    background:
      radial-gradient(circle at 41% 81%, rgba(255,250,240,0.9) 0, rgba(255,220,190,0.5) 40px, rgba(255,200,160,0) 160px),
      linear-gradient(180deg,
        var(--sky-deep) 0%,
        var(--sky-mid) 30%,
        var(--dusk-violet) 52%,
        var(--dusk-rose) 63%,
        var(--sunset-peach) 72%,
        var(--sunset-orange) 80%,
        var(--ember) 86%,
        var(--night) 96%);
  }
  .cover-frame {
    position: absolute;
    left: 45px;
    top: 45px;
    width: 1104px;
    height: 1104px;
    border: 3px solid var(--frame);
    border-radius: 2px;
    box-sizing: border-box;
  }
  .cover-text {
    position: absolute;
    left: 96px;
    top: 940px;
  }
  .album-title {
    margin: 0;
    font-family: "Montserrat", sans-serif;
    font-weight: 700;
    font-size: 44px;
    line-height: 1;
    letter-spacing: -0.01em;
    color: var(--title);
    white-space: nowrap;
  }
  .artist-name {
    margin: 14px 0 0;
    font-family: "Montserrat", sans-serif;
    font-weight: 300;
    font-size: 52px;
    line-height: 1;
    letter-spacing: 0.46em;
    color: var(--artist);
    white-space: nowrap;
  }
</style>
</head>
<body>
  <main class="album-cover">
    <div class="cover-photo" role="img" aria-label="Photograph: sunset sky over dark hills, a flag at half-staff on a tall pole at left and a battlefield cross silhouette on the ridge at right"></div>
    <div class="cover-frame"></div>
    <div class="cover-text">
      <h1 class="album-title">Lanterns, Orchards, and Harvests</h1>
      <p class="artist-name">DANIEL HARROW</p>
    </div>
  </main>
</body>
</html>
```